A new customer-driven VC fund for Enterprise IT Startups

I am bringing together a global group of customers (CIOs, CTOs, CISOs of Beacon 3000 companies) to help me identify and diligence best-of-breed Enterprise IT startups so I can invest in them via my new venture capital fund, Larkfen Ventures. In many ways, this is a new model for a VC fund and my goal is to revolutionize Venture Capital so that we hit the bull's eye in investing way more often in what is otherwise a guessing game for most VCs. So in the website, I'd like to capture the essences of global reach, best-of-breed, breakthrough innovation. I also want it to convey the ability of Larkfen Ventures to create category winners (i.e., if you want to be a market leader as a startup, you must take an investment from Larkfen Ventures).
My current website is www.larkfen-ventures.example - please use the content from the website within your design but please DO NOT use the design elements from the current website. INSTEAD, I'm looking for new and creative ideas on how I can leverage the existing content in a more appealing design -- any designs that look remotely similar to the existing website will be immediately declined.
I also want to ensure that the web design is mobile friendly.
Target Market(s)
Startup founders, potential investors, and other VCs
Industry/Entity Type
Venture Capital
Coding
Coded - Design and coding required
Number of Pages Required
1 page
Look and feel
Each slider illustrates characteristics of the customer's brand and the style your logo design should communicate.

```html
<!DOCTYPE html>
<html lang="en">
<head>
<meta charset="utf-8">
<title>Larkfen Ventures — Enterprise IT Venture Fund</title>
<link href="https://fonts.googleapis.com/css2?family=Poppins:wght@400;500;600;700&family=Open+Sans:wght@400;600&display=swap" rel="stylesheet">
<style>
:root{
  --navy:#0a1a4f;
  --navy-deep:#06123a;
  --blue:#1d4fd6;
  --blue-soft:#3b6cf0;
  --sky:#e8eefb;
  --panel:#f3f6fc;
  --ink:#1b2440;
  --muted:#6b7590;
  --line:#d9e0ef;
  --white:#ffffff;
}
*{box-sizing:border-box;margin:0;padding:0}
html,body{width:1200px;height:3528px;overflow:hidden;background:var(--white)}
body{font-family:"Open Sans",Arial,sans-serif;color:var(--ink);font-size:13px;line-height:1.6}
h1,h2,h3,h4,.brand,.nav a,.stat-value{font-family:"Poppins",Arial,sans-serif}
.wrap{width:1060px;margin:0 auto;position:relative}

/* Hero */
.hero{height:613px;background:linear-gradient(120deg,var(--navy-deep) 0%,var(--navy) 55%,#123a9a 100%);position:relative;overflow:hidden;color:var(--white)}
.hero-art{position:absolute;right:0;top:0;width:760px;height:613px;background:radial-gradient(circle at 60% 75%,rgba(80,140,255,.55) 0%,rgba(30,70,180,.25) 35%,rgba(10,26,79,0) 70%)}
.nav{height:78px;display:flex;align-items:center;justify-content:space-between;position:relative;z-index:2}
.brand{display:flex;align-items:center;gap:10px;font-weight:600;font-size:20px;color:var(--white)}
.brand-dot{width:14px;height:14px;border-radius:50%;background:var(--blue-soft)}
.nav ul{display:flex;list-style:none;gap:34px;align-items:center}
.nav a{color:var(--white);text-decoration:none;font-size:12px;font-weight:500;letter-spacing:.5px;text-transform:uppercase}
.nav .cta{background:var(--blue);padding:10px 20px;border-radius:3px}
.hero-copy{position:relative;z-index:2;padding-top:120px;width:620px}
.hero-copy h1{font-size:44px;line-height:1.18;font-weight:700}
.hero-copy p{margin-top:22px;font-size:13px;color:#c8d3f0;width:600px}
.btn-outline{display:inline-block;margin-top:26px;border:1px solid var(--white);color:var(--white);font-size:11px;padding:8px 18px;text-transform:uppercase;letter-spacing:1px}

/* Section heading */
.eyebrow{width:22px;height:4px;background:var(--blue);margin-bottom:10px}
.section-title{font-size:32px;font-weight:700;color:var(--navy)}
.section-lead{color:var(--muted);margin-top:6px;font-size:13px}

/* Who we are */
.who{height:511px;padding-top:60px;background:var(--white)}
.who-cards{display:grid;grid-template-columns:repeat(3,1fr);gap:34px;margin-top:36px}
.card{background:var(--white);border:1px solid var(--line);box-shadow:0 8px 24px rgba(20,40,100,.07);padding:26px;border-radius:4px}
.card:nth-child(2){margin-top:50px}
.card:nth-child(3){margin-top:24px}
.card h3{font-size:13px;font-weight:600;color:var(--navy);text-transform:uppercase;margin:12px 0 8px}
.card p{color:var(--muted);font-size:12px}
.icon{width:36px;height:36px}

/* Strength */
.strength{height:818px;background:var(--panel);padding-top:56px;position:relative}
.strength-band{position:absolute;left:0;right:0;top:0;height:150px;background:linear-gradient(180deg,#d6e1f7,var(--panel))}
.strength .wrap{z-index:1}
.sub-title{font-family:"Poppins",Arial,sans-serif;font-weight:600;font-size:15px;color:var(--navy);margin-top:18px}
.focus{display:grid;grid-template-columns:repeat(6,1fr);gap:16px;margin-top:20px}
.focus-item{background:var(--white);border:1px solid var(--line);height:120px;display:flex;flex-direction:column;align-items:center;justify-content:center;gap:12px;font-size:12px;font-weight:600;color:var(--navy);text-align:center;padding:0 8px}
.focus-item.active{background:var(--blue);color:var(--white);border-color:var(--blue)}
.stats-intro{font-family:"Poppins",Arial,sans-serif;font-size:18px;font-weight:600;color:var(--navy);margin-top:44px;width:760px;line-height:1.4}
.stats{display:grid;grid-template-columns:repeat(4,1fr);gap:18px;margin-top:26px}
.stat{background:var(--white);border:1px solid var(--line);padding:24px 20px;text-align:center;height:150px}
.stat-value{font-size:30px;font-weight:700;color:var(--blue)}
.stat p{font-size:12px;color:var(--muted);margin-top:6px}
.themes{display:grid;grid-template-columns:repeat(3,1fr);gap:18px;margin-top:18px}
.theme{display:flex;align-items:center;gap:16px;background:var(--white);border:1px solid var(--line);padding:18px 20px;font-size:12px;color:var(--ink)}

/* Team */
.team{height:408px;padding-top:50px}
.team-head{display:flex;justify-content:space-between;align-items:flex-end}
.arrows{display:flex;gap:6px}
.arrows span{width:34px;height:34px;border:1px solid var(--line);display:flex;align-items:center;justify-content:center}
.arrows span.on{background:var(--blue);border-color:var(--blue)}
.team-grid{display:grid;grid-template-columns:repeat(4,1fr);gap:30px;margin-top:28px}
.member{position:relative;height:210px;border-radius:3px;overflow:hidden}
.member-photo{position:absolute;inset:0;background:linear-gradient(160deg,#8d95a8,#3c4560)}
.member-info{position:absolute;left:0;right:0;bottom:0;padding:12px 14px;background:linear-gradient(0deg,rgba(6,18,58,.9),rgba(6,18,58,0));color:var(--white)}
.member-info h4{font-size:14px;font-weight:600}
.member-info span{font-size:11px;color:#c8d3f0}

/* Engine */
.engine{height:512px;background:var(--panel);padding-top:56px}
.engine-cards{display:grid;grid-template-columns:repeat(3,1fr);gap:34px;margin-top:36px}
.engine-cards .card:nth-child(2){margin-top:-10px}
.engine-cards .card:nth-child(3){margin-top:30px}

/* Inquiry */
.inquiry{height:358px;padding-top:56px;text-align:center}
.inquiry .section-title{font-size:30px}
.form{display:grid;grid-template-columns:repeat(3,1fr);gap:16px 22px;width:860px;margin:34px auto 0;text-align:left}
.field label{font-size:11px;color:var(--muted);display:block;margin-bottom:4px}
.field .box{height:36px;border:1px solid var(--line);background:var(--white)}
.field.tall{grid-row:span 2}
.field.tall .box{height:92px}
.submit{display:inline-block;margin-top:24px;background:var(--blue);color:var(--white);font-size:11px;padding:9px 28px;text-transform:uppercase;letter-spacing:1px;font-family:"Poppins",Arial,sans-serif}

/* Footer */
.footer{height:308px;background:var(--navy-deep);color:#c8d3f0;position:relative}
.footer-grid{display:grid;grid-template-columns:1.2fr 1fr 1fr 1.1fr;gap:40px;padding-top:56px}
.footer .brand{font-size:22px}
.footer h4{color:var(--white);font-size:13px;font-weight:600;margin-bottom:14px;text-transform:uppercase}
.footer li{list-style:none;font-size:12px;margin-bottom:8px;display:flex;gap:8px;align-items:center}
.socials{display:flex;gap:8px;margin-top:20px}
.socials span{width:26px;height:26px;border-radius:50%;border:1px solid #4a5a8c}
.map{height:120px;background:linear-gradient(135deg,#c9d3e6,#9fb0cf)}
.copyright{position:absolute;left:0;right:0;bottom:0;height:34px;background:var(--blue);color:var(--white);font-size:11px;text-align:center;line-height:34px}
</style>
</head>
<body>

<header class="hero">
  <div class="hero-art" role="img" aria-label="Glowing digital globe with network connections over a dark blue field"></div>
  <div class="wrap">
    <nav class="nav">
      <div class="brand"><span class="brand-dot"></span>Larkfen Ventures</div>
      <ul>
        <li><a href="#about">About</a></li>
        <li><a href="#network">Network</a></li>
        <li><a href="#advisors">Public Advisors</a></li>
        <li><a href="#strategies">Strategies</a></li>
        <li><a class="cta" href="#contact">Contact Us</a></li>
      </ul>
    </nav>
    <div class="hero-copy">
      <h1>We Invest in Enterprise IT Startups at the Product-Market-Fit Stage.</h1>
      <p>We bring early-stage founders together with a global network of Beacon 3000 technology leaders who help us identify, diligence and scale best-of-breed enterprise software, turning breakthrough products into lasting category winners.</p>
      <a class="btn-outline" href="#contact">Contact Us</a>
    </div>
  </div>
</header>

<section class="who" id="about">
  <div class="wrap">
    <div class="eyebrow"></div>
    <h2 class="section-title">Who We Are</h2>
    <p class="section-lead">We fund a new breed of startups, guided by the customers who will buy from them at scale.</p>
    <div class="who-cards">
      <article class="card">
        <svg class="icon" viewBox="0 0 36 36"><circle cx="13" cy="13" r="6" fill="none" stroke="#1d4fd6" stroke-width="2"/><circle cx="25" cy="15" r="4" fill="none" stroke="#1d4fd6" stroke-width="2"/><path d="M3 31c1-7 6-10 10-10s9 3 10 10M21 31c1-5 3-7 6-7s5 2 6 7" fill="none" stroke="#1d4fd6" stroke-width="2"/></svg>
        <h3>Customers</h3>
        <p>Hundreds of technology executives from the largest global enterprises share their buying plans, test products and tell us which startups truly solve their most urgent problems.</p>
      </article>
      <article class="card">
        <svg class="icon" viewBox="0 0 36 36"><circle cx="18" cy="18" r="14" fill="none" stroke="#1d4fd6" stroke-width="2"/><circle cx="18" cy="18" r="8" fill="none" stroke="#1d4fd6" stroke-width="2"/><circle cx="18" cy="18" r="2.5" fill="#1d4fd6"/></svg>
        <h3>Our Investment Philosophy</h3>
        <p>We back companies that already have product-market fit and help them win their category faster through real customer demand, focused coaching and a global go-to-market network.</p>
      </article>
      <article class="card">
        <svg class="icon" viewBox="0 0 36 36"><path d="M6 20l8 8 16-18" fill="none" stroke="#1d4fd6" stroke-width="2.5"/><rect x="2" y="2" width="32" height="32" rx="4" fill="none" stroke="#1d4fd6" stroke-width="2"/></svg>
        <h3>Customer-Led Investments</h3>
        <p>Every deal is sourced and validated with input from buyers, so our portfolio companies gain trusted references and early revenue from the very first day.</p>
      </article>
    </div>
  </div>
</section>

<section class="strength" id="network">
  <div class="strength-band"></div>
  <div class="wrap">
    <div class="eyebrow"></div>
    <h2 class="section-title">Strength In Numbers</h2>
    <p class="sub-title">Investment Focus Areas</p>
    <div class="focus">
      <div class="focus-item"><svg class="icon" viewBox="0 0 36 36"><path d="M18 3l12 5v9c0 8-6 13-12 16-6-3-12-8-12-16V8z" fill="none" stroke="#1d4fd6" stroke-width="2"/></svg>Security</div>
      <div class="focus-item"><svg class="icon" viewBox="0 0 36 36"><rect x="8" y="8" width="20" height="20" rx="3" fill="none" stroke="#1d4fd6" stroke-width="2"/><path d="M14 2v6M22 2v6M14 28v6M22 28v6M2 14h6M2 22h6M28 14h6M28 22h6" stroke="#1d4fd6" stroke-width="2"/></svg>AI &amp; Data</div>
      <div class="focus-item active"><svg class="icon" viewBox="0 0 36 36"><circle cx="18" cy="6" r="4" fill="none" stroke="#fff" stroke-width="2"/><circle cx="6" cy="28" r="4" fill="none" stroke="#fff" stroke-width="2"/><circle cx="30" cy="28" r="4" fill="none" stroke="#fff" stroke-width="2"/><path d="M16 10L8 24M20 10l8 14M10 28h16" stroke="#fff" stroke-width="2"/></svg>Networking &amp; Architecture</div>
      <div class="focus-item"><svg class="icon" viewBox="0 0 36 36"><path d="M10 26a7 7 0 010-14 9 9 0 0117 2 6 6 0 01-1 12z" fill="none" stroke="#1d4fd6" stroke-width="2"/></svg>Cloud &amp; Infrastructure</div>
      <div class="focus-item"><svg class="icon" viewBox="0 0 36 36"><ellipse cx="18" cy="8" rx="12" ry="4" fill="none" stroke="#1d4fd6" stroke-width="2"/><path d="M6 8v20c0 2 5 4 12 4s12-2 12-4V8M6 18c0 2 5 4 12 4s12-2 12-4" fill="none" stroke="#1d4fd6" stroke-width="2"/></svg>Storage</div>
      <div class="focus-item"><svg class="icon" viewBox="0 0 36 36"><rect x="3" y="6" width="30" height="20" rx="2" fill="none" stroke="#1d4fd6" stroke-width="2"/><path d="M12 32h12M18 26v6" stroke="#1d4fd6" stroke-width="2"/></svg>SaaS</div>
    </div>

    <p class="stats-intro">We collect and analyze monthly purchase intent data from a global network of IT decision-makers.</p>
    <div class="stats">
      <div class="stat"><div class="stat-value">500+</div><p>Senior technology executives sharing monthly buying intent with our team</p></div>
      <div class="stat"><div class="stat-value">$100B+</div><p>Combined annual IT spend represented across our customer network</p></div>
      <div class="stat"><div class="stat-value">15</div><p>Countries and industries covered by our advisor community</p></div>
      <div class="stat"><div class="stat-value">550+</div><p>Startups reviewed and scored by buyers each year</p></div>
    </div>

    <p class="sub-title" style="margin-top:34px">Unifying Investment Themes:</p>
    <div class="themes">
      <div class="theme"><svg class="icon" viewBox="0 0 36 36"><path d="M4 26l9-9 6 6 13-13" fill="none" stroke="#1d4fd6" stroke-width="2.5"/></svg>Real Cost Reduction in Operations</div>
      <div class="theme"><svg class="icon" viewBox="0 0 36 36"><path d="M18 3l4 10h10l-8 7 3 11-9-6-9 6 3-11-8-7h10z" fill="none" stroke="#1d4fd6" stroke-width="2"/></svg>Delivering Large Gains Through Enhanced Automation</div>
      <div class="theme"><svg class="icon" viewBox="0 0 36 36"><rect x="4" y="4" width="12" height="12" fill="none" stroke="#1d4fd6" stroke-width="2"/><rect x="20" y="20" width="12" height="12" fill="none" stroke="#1d4fd6" stroke-width="2"/><path d="M16 10h10v10" fill="none" stroke="#1d4fd6" stroke-width="2"/></svg>Products and Platforms That Solve a Specific Problem</div>
    </div>
  </div>
</section>

<section class="team" id="advisors">
  <div class="wrap">
    <div class="team-head">
      <div><div class="eyebrow"></div><h2 class="section-title">Team, Investors &amp; Advisors</h2></div>
      <div class="arrows">
        <span><svg width="12" height="12" viewBox="0 0 12 12"><path d="M8 1L3 6l5 5" fill="none" stroke="#1d4fd6" stroke-width="2"/></svg></span>
        <span class="on"><svg width="12" height="12" viewBox="0 0 12 12"><path d="M4 1l5 5-5 5" fill="none" stroke="#fff" stroke-width="2"/></svg></span>
      </div>
    </div>
    <div class="team-grid">
      <div class="member"><div class="member-photo" role="img" aria-label="Portrait photo of the fund's founder"></div><div class="member-info"><h4>Ravi Anand</h4><span>Founder &amp; General Partner</span></div></div>
      <div class="member"><div class="member-photo" role="img" aria-label="Portrait photo of an investor"></div><div class="member-info"><h4>Martin Hale</h4><span>Limited Partner</span></div></div>
      <div class="member"><div class="member-photo" role="img" aria-label="Portrait photo of an advisor"></div><div class="member-info"><h4>Vikram Sethi</h4><span>Strategic Advisor</span></div></div>
      <div class="member"><div class="member-photo" role="img" aria-label="Portrait photo of an advisor"></div><div class="member-info"><h4>Thomas Grieve</h4><span>Operating Advisor</span></div></div>
    </div>
  </div>
</section>

<section class="engine" id="strategies">
  <div class="wrap">
    <div class="eyebrow"></div>
    <h2 class="section-title">A Global GTM Engine</h2>
    <p class="section-lead">We don't just invest "customer dollars" — we partner with you at each step of the way to help you navigate the complex landscape of enterprise sales.</p>
    <div class="engine-cards">
      <article class="card">
        <svg class="icon" viewBox="0 0 36 36"><circle cx="18" cy="12" r="7" fill="none" stroke="#1d4fd6" stroke-width="2"/><path d="M6 33c1-8 6-12 12-12s11 4 12 12" fill="none" stroke="#1d4fd6" stroke-width="2"/></svg>
        <h3>GTM Coaching</h3>
        <p>Our operators work with founders on pricing, positioning, sales hiring and pipeline building so every team can sell with confidence to large enterprises.</p>
      </article>
      <article class="card">
        <svg class="icon" viewBox="0 0 36 36"><path d="M3 18l7-7 8 6 8-6 7 7-15 13z" fill="none" stroke="#1d4fd6" stroke-width="2"/></svg>
        <h3>Strategic Partners</h3>
        <p>Leading integrators, resellers and cloud providers in our network open doors to channels that would otherwise take founders years to reach alone.</p>
      </article>
      <article class="card">
        <svg class="icon" viewBox="0 0 36 36"><circle cx="18" cy="18" r="14" fill="none" stroke="#1d4fd6" stroke-width="2"/><path d="M4 18h28M18 4c5 5 5 23 0 28M18 4c-5 5-5 23 0 28" fill="none" stroke="#1d4fd6" stroke-width="2"/></svg>
        <h3>Global Ambassadors</h3>
        <p>Regional ambassadors across every continent introduce our companies to local buyers and help them expand internationally with trusted support.</p>
      </article>
    </div>
  </div>
</section>

<section class="inquiry" id="contact">
  <div class="wrap">
    <h2 class="section-title">Quick Inquiry</h2>
    <form class="form">
      <div class="field"><label>First Name</label><div class="box"></div></div>
      <div class="field"><label>Email</label><div class="box"></div></div>
      <div class="field tall"><label>Your Message</label><div class="box"></div></div>
      <div class="field"><label>Phone Number</label><div class="box"></div></div>
      <div class="field"><label>Last Name</label><div class="box"></div></div>
    </form>
    <span class="submit">Submit</span>
  </div>
</section>

<footer class="footer">
  <div class="wrap footer-grid">
    <div>
      <div class="brand"><span class="brand-dot"></span>Larkfen Ventures</div>
      <div class="socials"><span></span><span></span><span></span><span></span></div>
    </div>
    <div>
      <h4>Contact Info</h4>
      <ul>
        <li><svg width="12" height="12" viewBox="0 0 12 12"><path d="M2 1h3l1 3-2 1c1 2 2 3 4 4l1-2 3 1v3c-6 0-10-4-10-10z" fill="#3b6cf0"/></svg>+1 (555) 014-2290</li>
        <li><svg width="12" height="12" viewBox="0 0 12 12"><rect x="1" y="2" width="10" height="8" fill="none" stroke="#3b6cf0"/><path d="M1 2l5 4 5-4" fill="none" stroke="#3b6cf0"/></svg>hello@larkfen-ventures.example</li>
        <li><svg width="12" height="12" viewBox="0 0 12 12"><path d="M6 11S2 7 2 4.5a4 4 0 018 0C10 7 6 11 6 11z" fill="#3b6cf0"/></svg>200 Harbor Lane, Palo Alto</li>
      </ul>
    </div>
    <div>
      <h4>Quick Links</h4>
      <ul>
        <li>About</li>
        <li>Network</li>
        <li>Team &amp; Advisors</li>
        <li>Strategies</li>
      </ul>
    </div>
    <div class="map" role="img" aria-label="Small map showing the office location"></div>
  </div>
  <div class="copyright">Copyright © 2024 Larkfen Ventures. All Rights Reserved.</div>
</footer>

</body>
</html>
```